QuellbridgeSystemsApp Explainer

We are looking for an attractive/moderan info graphics that will explain our software and how it helps driving schools to fully integrated their business with clients and staff.
Attached word doc outlines the description of the main modules and most important services that our software performs.
The info graphic should be easy to read and understand as the main audience of school owners is not technically savvy and are generally averse to technology and computers.

Target Market(s)

Driving school owners and managers

Industry/Entity Type

Driving School

Font styles to use
Sans Serif

Colors

Designer to choose colors to be used in the design.

Requirements
Must have
• Clear graphics that complement logo colors. Easy to read understand.
Should not have
• complicated and confusing text.

```html
<!DOCTYPE html>
<html lang="en">
<head>
<meta charset="utf-8">
<title>QuellbridgeSystemsApp Explainer</title>
<link rel="stylesheet" href="https://fonts.googleapis.com/css2?family=Ubuntu:wght@400;500;700&family=Arimo:wght@400&display=swap">
<style>
  :root {
    --brand-green: #52b848;
    --band-green: #4db933;
    --icon-green: #4aae32;
    --ink: #333333;
    --soft-bg: #fdfdf8;
    --white: #ffffff;
  }
  * { margin: 0; padding: 0; box-sizing: border-box; }
  html, body {
    width: 1200px;
    height: 2200px;
    overflow: hidden;
    background: var(--white);
  }
  .infographic {
    position: relative;
    width: 1200px;
    height: 2200px;
    overflow: hidden;
    background: var(--white);
    font-family: "Arimo", Arial, sans-serif;
    color: var(--ink);
  }
  .hero {
    position: absolute;
    left: 0; top: 0;
    width: 1200px; height: 540px;
    background: var(--brand-green);
  }
  .hero-mark {
    position: absolute;
    left: 462px; top: 20px;
    width: 276px; height: 276px;
    border-radius: 50%;
    background: var(--white);
  }
  .hero-name {
    position: absolute;
    left: 0; top: 330px;
    width: 1200px;
    text-align: center;
    font-family: "Ubuntu", sans-serif;
    font-weight: 700;
    font-size: 84px;
    letter-spacing: -1px;
    color: var(--white);
  }
  .section-band {
    position: absolute;
    left: 0;
    width: 1200px;
    height: 85px;
    background: var(--band-green);
    color: var(--white);
    font-family: "Ubuntu", sans-serif;
    font-weight: 700;
    font-size: 52px;
    line-height: 85px;
    text-align: center;
  }
  .modules-panel {
    position: absolute;
    left: 0; top: 681px;
    width: 1200px; height: 384px;
    background: var(--soft-bg);
  }
  .module {
    position: absolute;
    top: 40px;
    width: 280px;
    margin-left: -140px;
    text-align: center;
  }
  .module-icon {
    display: block;
    width: 166px; height: 166px;
    margin: 0 auto;
  }
  .module-label {
    margin-top: 28px;
    font-family: "Ubuntu", sans-serif;
    font-weight: 400;
    font-size: 25px;
    line-height: 31px;
    color: var(--ink);
  }
  .feature-list {
    position: absolute;
    left: 80px;
    width: 1080px;
    list-style: none;
    font-size: 27px;
    line-height: 40.5px;
    color: var(--ink);
  }
  .feature-list li { position: relative; }
  .feature-list li::before {
    content: "";
    position: absolute;
    left: -23px; top: 18px;
    width: 7px; height: 7px;
    border-radius: 50%;
    background: var(--band-green);
  }
</style>
</head>
<body>
<main class="infographic">

  <header class="hero">
    <div class="hero-mark"></div>
    <div class="hero-name">QuellbridgeSystemsApp</div>
  </header>

  <h2 class="section-band" style="top:596px;">Modules</h2>

  <section class="modules-panel">
    <div class="module" style="left:175px;">
      <svg class="module-icon" viewBox="0 0 166 166" aria-hidden="true">
        <circle cx="83" cy="83" r="79" fill="none" stroke="var(--icon-green)" stroke-width="6"/>
        <path d="M39 50 h30 l6 8 h51 v8 H39 z" fill="var(--icon-green)"/>
        <rect x="39" y="70" width="87" height="45" fill="var(--icon-green)"/>
      </svg>
      <div class="module-label">Administrative</div>
    </div>

    <div class="module" style="left:460px;">
      <svg class="module-icon" viewBox="0 0 166 166" aria-hidden="true">
        <circle cx="83" cy="83" r="79" fill="none" stroke="var(--icon-green)" stroke-width="6"/>
        <circle cx="83" cy="64" r="16" fill="none" stroke="var(--icon-green)" stroke-width="4"/>
        <path d="M48 117 v-8 c0-12 10-20 22-20 h26 c12 0 22 8 22 20 v8 z" fill="none" stroke="var(--icon-green)" stroke-width="4" stroke-linejoin="round"/>
      </svg>
      <div class="module-label">Website<br>Enrolment</div>
    </div>

    <div class="module" style="left:745px;">
      <svg class="module-icon" viewBox="0 0 166 166" aria-hidden="true">
        <circle cx="83" cy="83" r="79" fill="none" stroke="var(--icon-green)" stroke-width="6"/>
        <circle cx="83" cy="83" r="37" fill="var(--icon-green)"/>
        <circle cx="77" cy="72" r="8" fill="var(--white)"/>
        <path d="M63 100 c0-12 6-18 14-18 s12 6 12 18 z" fill="var(--white)"/>
        <circle cx="92" cy="80" r="6" fill="var(--white)"/>
        <path d="M84 101 c0-10 4-15 9-15 s9 5 9 15 z" fill="var(--white)"/>
      </svg>
      <div class="module-label">Student and<br>Parent Center</div>
    </div>

    <div class="module" style="left:1032px;">
      <svg class="module-icon" viewBox="0 0 166 166" aria-hidden="true">
        <circle cx="83" cy="83" r="79" fill="none" stroke="var(--icon-green)" stroke-width="6"/>
        <rect x="61" y="34" width="44" height="92" rx="6" fill="none" stroke="var(--icon-green)" stroke-width="4"/>
        <line x1="61" y1="46" x2="105" y2="46" stroke="var(--icon-green)" stroke-width="3"/>
        <line x1="61" y1="114" x2="105" y2="114" stroke="var(--icon-green)" stroke-width="3"/>
      </svg>
      <div class="module-label">Instructor and<br>Staff Smart<br>phone access</div>
    </div>
  </section>

  <h2 class="section-band" style="top:1065px;">Administrative</h2>
  <ul class="feature-list" style="top:1198px;">
    <li>Accomplish all important administrative functions</li>
    <li>Create student accounts, enroll them and manage student payments</li>
    <li>Create lessons and classroom</li>
    <li>Run business reports</li>
    <li>Create State Forms for compliance</li>
    <li>Schedule Student lessons and take classroom attendance</li>
    <li>Track vehicles via GPS and manage vehicle maintenance</li>
    <li>Send and receive text messages from students and parents</li>
  </ul>

  <h2 class="section-band" style="top:1581px;">Website Enrolment</h2>
  <ul class="feature-list" style="top:1714px;">
    <li>Receive enrolments directly from their website</li>
    <li>Save all enrolment information directly into the schools' database</li>
    <li>Process credit card payments</li>
    <li>Create student accounts automatically</li>
  </ul>

  <h2 class="section-band" style="top:1932px;">Student Parent Center</h2>
  <ul class="feature-list" style="top:2065px;">
    <li>Students access their own account</li>
    <li>Pay for any open balances</li>
    <li>View the status of their program</li>
    <li>Purchase additional lessons</li>
  </ul>

</main>
</body>
</html>
```